UK Supplement Company Needs a Label for Diet Protein Powder

We need a new, modern and fresh design for our Diet Protein Powder. Our protein powder is packaged in black plastic tubs (photo attached) and needs an attractive label. We would like to see designs that grab attention and look professional. We're very open to ideas. The label should be 88mm x 365mm. We also prefer PSD format where possible. These alterations could be made once your design is chosen. Have attached photo of our shake ingredients/benefits.
Updates

Need extra days to review

Target Market(s)

Slimmers

Industry/Entity Type

Health And Wellness

Font styles to use
Serif
Sans Serif

Colors

Designer to choose colors to be used in the design.

Requirements
Must have
• Clean, Modern and Professional Look. Eye catching. The flavour, we offer 6 flavours so this must be something we can edit (Flavours are Banana, Chocolate, Chocolate Mint, Strawberry, Toffee and Vanilla).
Nice to have
• Our logo, this can be BRISK Nutrition or just BRISK. Our logo files are attached.
Should not have
• We do not want to see people (faces or bodies) on the design.

```html
<!DOCTYPE html>
<html lang="en">
<head>
<meta charset="utf-8">
<title>BRISK Nutrition – Lean Shake Formula Label</title>
<link rel="stylesheet" href="https://fonts.googleapis.com/css2?family=Roboto+Condensed:wght@300;400;500;700&family=Roboto:wght@500;700;900&display=swap">
<style>
  :root {
    --page: #f4f4f4;
    --label-black: #0c0d0e;
    --band-blue: #3aa7c9;
    --band-blue-deep: #2a93b8;
    --lime: #b6d136;
    --panel-green: #9cb65b;
    --panel-ink: #e9f0d6;
    --title-grey: #e3e5e6;
    --ink-dark: #141618;
    --muted: #a9abad;
    --flavour-red: #d9464b;
    --brand-blue: #3aa7c9;
  }
  * { margin: 0; padding: 0; box-sizing: border-box; }
  html, body { width: 1200px; height: 1014px; overflow: hidden; background: var(--page); }
  .canvas { position: relative; width: 1200px; height: 1014px; }

  .label {
    position: absolute; left: 110px; top: 82px;
    width: 980px; height: 850px;
    background: var(--label-black);
    overflow: hidden;
    font-family: "Roboto Condensed", "Arial Narrow", sans-serif;
  }

  .brand { position: absolute; left: 107px; top: 56px; }
  .brand-name {
    display: block;
    font-family: "Roboto", Arial, sans-serif;
    font-weight: 900; font-size: 112px; line-height: 1;
    color: var(--brand-blue); letter-spacing: -2px;
  }
  .brand-sub {
    display: block; margin-top: 14px;
    font-family: "Roboto", Arial, sans-serif;
    font-weight: 700; font-size: 19px; letter-spacing: 17px;
    color: var(--lime);
  }

  .title-band {
    position: absolute; left: 0; top: 244px;
    width: 870px; height: 398px;
    background: linear-gradient(90deg, var(--band-blue-deep), var(--band-blue));
    border-radius: 0 38px 38px 0;
  }
  .title-top, .title-bottom {
    position: absolute; left: 107px;
    font-family: "Roboto", Arial, sans-serif; font-weight: 700;
    color: var(--ink-dark); line-height: 1;
  }
  .title-top { top: 30px; font-size: 84px; }
  .title-main {
    position: absolute; left: 100px; top: 95px;
    font-weight: 400; font-size: 214px; line-height: 1;
    color: var(--title-grey); letter-spacing: -2px;
  }
  .title-bottom { top: 296px; font-size: 82px; }

  .claims {
    position: absolute; left: 107px; top: 670px;
    font-family: "Roboto", Arial, sans-serif; font-weight: 500;
    font-size: 31px; color: var(--lime); white-space: nowrap;
  }
  .claims .divider { color: #e8e8e8; margin: 0 28px; }

  .net-weight {
    position: absolute; left: 107px; top: 778px;
    font-size: 23px; color: var(--muted);
  }

  .flavour-tag {
    position: absolute; left: 581px; top: 770px;
    width: 289px; height: 80px;
    background: var(--flavour-red);
    border-radius: 8px 8px 0 0;
    display: flex; align-items: center; justify-content: center;
    padding-bottom: 6px;
    font-family: "Roboto", Arial, sans-serif; font-weight: 500;
    font-size: 27px; letter-spacing: 3px; color: #1c1112;
  }

  .stats-panel {
    position: absolute; left: 871px; top: 18px;
    width: 88px; height: 463px;
    background: var(--panel-green);
    border-radius: 6px;
    display: flex; flex-direction: column; align-items: center;
    padding: 28px 8px 0;
    color: var(--panel-ink); text-align: center;
  }
  .stat { width: 100%; padding: 8px 0 10px; border-bottom: 2px solid rgba(233,240,214,0.55); }
  .stat:last-child { border-bottom: none; }
  .stat-value { display: block; font-weight: 500; font-size: 36px; line-height: 1; white-space: nowrap; }
  .stat-unit { font-size: 20px; }
  .stat-label { display: block; font-size: 13px; letter-spacing: 0.5px; margin-top: 4px; text-transform: uppercase; line-height: 1.2; }
</style>
</head>
<body>
<div class="canvas">
  <section class="label" aria-label="Lean Shake Formula tub label">
    <div class="brand">
      <span class="brand-name">BRISK</span>
      <span class="brand-sub">NUTRITION</span>
    </div>

    <div class="title-band">
      <span class="title-top">LEAN</span>
      <span class="title-main">SHAKE</span>
      <span class="title-bottom">FORMULA</span>
    </div>

    <p class="claims">High Protein<span class="divider">|</span>Low Carbohydrates</p>

    <p class="net-weight">NET WT. 6lb (2.727G)</p>

    <div class="flavour-tag">STRAWBERRY</div>

    <aside class="stats-panel">
      <div class="stat"><span class="stat-value">1050</span><span class="stat-label">Calories</span></div>
      <div class="stat"><span class="stat-value">60G</span><span class="stat-label">Protein</span></div>
      <div class="stat"><span class="stat-value">250<span class="stat-unit">G+</span></span><span class="stat-label">Carbs</span></div>
      <div class="stat"><span class="stat-value">30</span><span class="stat-label">Vitamins &amp; Minerals</span></div>
    </aside>
  </section>
</div>
</body>
</html>
```